Business card for new consulting business - Brackenvale Enterprises Pty Ltd.

Consulting in the areas of Occupational Health, Safety and Community Relations in the resources (mining) industries. The consultant (me) will work both within Australia and overseas jurisdictions such as South East Asia, Africa , South America etc, often working with third world indigenous communities. The design should suggest a high level of social and environmental responsibility.

```html
<!DOCTYPE html>
<html lang="en">
<head>
<meta charset="utf-8">
<title>Brackenvale Enterprises Pty Ltd – Stationery</title>
<link rel="stylesheet" href="https://fonts.googleapis.com/css2?family=Roboto:wght@400;500&display=swap">
<style>
  :root {
    --brand-blue: #1177bd;
    --brand-green: #2bb673;
    --paper: #ffffff;
    --backdrop: #f1f2f4;
    --ink: #1a6fae;
  }
  * { box-sizing: border-box; margin: 0; padding: 0; }
  html, body {
    width: 1200px; height: 1200px; overflow: hidden;
    background: var(--backdrop);
    font-family: "Roboto", Arial, sans-serif;
  }
  .canvas { position: relative; width: 1200px; height: 1200px; }
  .stationery-area { position: absolute; left: 0; top: 0; width: 1200px; height: 855px; background: var(--backdrop); }
  .logo-area { position: absolute; left: 0; top: 855px; width: 1200px; height: 345px; background: var(--paper); }

  .card, .letterhead { position: absolute; background: var(--paper); overflow: hidden; }
  .card { width: 396px; height: 232px; left: 64px; }
  .card--front { top: 158px; }
  .card--back { top: 453px; background: var(--brand-blue); }
  .letterhead { left: 506px; top: 62px; width: 555px; height: 748px; }

  .band { position: absolute; left: 0; display: block; }

  .wordmark { position: absolute; display: flex; align-items: center; font-weight: 500; color: var(--brand-blue); }
  .wordmark__dot { border-radius: 50%; background: var(--brand-green); flex: none; }
  .wordmark__text { display: flex; flex-direction: column; line-height: 1; text-transform: uppercase; }
  .wordmark__primary { letter-spacing: 0.02em; }
  .wordmark__secondary { letter-spacing: 0.14em; margin-top: 3px; }

  .card-wordmark { left: 26px; top: 96px; gap: 7px; }
  .card-wordmark .wordmark__dot { width: 30px; height: 30px; }
  .card-wordmark .wordmark__primary { font-size: 17px; }
  .card-wordmark .wordmark__secondary { font-size: 8.5px; }

  .back-wordmark { left: 0; right: 0; top: 93px; justify-content: center; gap: 12px; color: var(--paper); }
  .back-wordmark .wordmark__dot { width: 52px; height: 52px; background: var(--paper); }
  .back-wordmark .wordmark__primary { font-size: 30px; }
  .back-wordmark .wordmark__secondary { font-size: 13px; margin-top: 5px; }

  .letter-wordmark { left: 0; right: 0; top: 78px; justify-content: center; gap: 7px; }
  .letter-wordmark .wordmark__dot { width: 34px; height: 34px; }
  .letter-wordmark .wordmark__primary { font-size: 19px; }
  .letter-wordmark .wordmark__secondary { font-size: 9px; }

  .master-wordmark { left: 0; right: 0; top: 148px; justify-content: center; gap: 18px; }
  .master-wordmark .wordmark__dot { width: 96px; height: 96px; }
  .master-wordmark .wordmark__primary { font-size: 50px; }
  .master-wordmark .wordmark__secondary { font-size: 22px; margin-top: 8px; color: var(--brand-blue); }

  .holder-name { position: absolute; color: var(--brand-green); font-weight: 500; font-size: 19px; letter-spacing: 0.01em; text-transform: uppercase; }
  .card .holder-name { left: 257px; top: 104px; }
  .letterhead .holder-name { left: 65px; top: 684px; font-size: 17px; }

  .contact-line { position: absolute; display: flex; gap: 12px; color: var(--ink); font-size: 9.5px; white-space: nowrap; }
  .contact-line b { font-weight: 500; margin-right: 3px; }
  .card .contact-line { left: 37px; top: 173px; }
  .letterhead .contact-line { left: 206px; top: 690px; font-size: 8.5px; gap: 10px; }
</style>
</head>
<body>
<main class="canvas">
  <section class="stationery-area">
    <article class="card card--front">
      <svg class="band band--top" width="396" height="27" viewBox="0 0 396 27"><polygon points="0,0 268,0 306,27 0,27" fill="var(--brand-blue)"/></svg>
      <div class="wordmark card-wordmark">
        <span class="wordmark__dot"></span>
        <span class="wordmark__text"><span class="wordmark__primary">Brackenvale</span><span class="wordmark__secondary">Enterprises Pty Ltd.</span></span>
      </div>
      <p class="holder-name">Your Name</p>
      <p class="contact-line">
        <span><b>A :</b>Your Address Comes Here</span>
        <span><b>P :</b>000-000-0000</span>
        <span><b>E :</b>info@brackenvale.com</span>
      </p>
      <svg class="band band--bottom" style="top:204px" width="396" height="28" viewBox="0 0 396 28"><polygon points="89,0 396,0 396,28 128,28" fill="var(--brand-green)"/></svg>
    </article>

    <article class="card card--back">
      <div class="wordmark back-wordmark">
        <span class="wordmark__dot"></span>
        <span class="wordmark__text"><span class="wordmark__primary">Brackenvale</span><span class="wordmark__secondary">Enterprises Pty Ltd.</span></span>
      </div>
    </article>

    <article class="letterhead">
      <svg class="band band--top" width="555" height="24" viewBox="0 0 555 24"><polygon points="0,0 430,0 464,24 0,24" fill="var(--brand-blue)"/></svg>
      <div class="wordmark letter-wordmark">
        <span class="wordmark__dot"></span>
        <span class="wordmark__text"><span class="wordmark__primary">Brackenvale</span><span class="wordmark__secondary">Enterprises Pty Ltd.</span></span>
      </div>
      <p class="holder-name">Your Name</p>
      <p class="contact-line">
        <span><b>A :</b>Your Address Comes Here</span>
        <span><b>P :</b>000-000-0000</span>
        <span><b>E :</b>info@brackenvale.com</span>
      </p>
      <svg class="band band--bottom" style="top:724px" width="555" height="24" viewBox="0 0 555 24"><polygon points="91,0 555,0 555,24 126,24" fill="var(--brand-green)"/></svg>
    </article>
  </section>

  <section class="logo-area">
    <div class="wordmark master-wordmark">
      <span class="wordmark__dot"></span>
      <span class="wordmark__text"><span class="wordmark__primary">Brackenvale</span><span class="wordmark__secondary">Enterprises Pty Ltd.</span></span>
    </div>
  </section>
</main>
</body>
</html>
```